Looking for an amazing business card for a thriving DJ business

We need a business card design for a DJ company based in South Florida. The DJ company specializes in weddings, parties, bar mitzvahs, corporate events, proms, and reunions. We are looking for a modern, simple business card design. The card should state DJ Marlow K.
Updates

The name on the card should be DJ Marlow K

Industry/Entity Type

Entertainment Industry

Contact Information for Business Card

DJ Marlow K
415.282.6047
bxdjmarlowk@quillmail.example
https://www.facebook-example.net/DjMarlowK/
https://www.photogram-example.net/djmarlow.k/
www.djmarlowk.example

Font styles to use
Serif
Sans Serif

Requirements
Must have
• My business card has to be awesome.
Should not have
• The card has to have personality.

```html
<!DOCTYPE html>
<html lang="en">
<head>
<meta charset="utf-8">
<title>DJ Marlow K — Business Card</title>
<link href="https://fonts.googleapis.com/css2?family=Playball&family=Quicksand:wght@300;400&display=swap" rel="stylesheet">
<style>
  :root {
    --backdrop: #333333;
    --card-top: #3a3a3a;
    --card-mid: #1e1e1e;
    --card-bottom: #161616;
    --gold: #c99a4e;
    --ink-light: #d6d6d6;
    --rule: #cfcfcf;
    --badge-bg: #ffffff;
    --badge-ink: #5a5f62;
  }
  * { margin: 0; padding: 0; box-sizing: border-box; }
  html, body {
    width: 1200px; height: 1200px; overflow: hidden;
    background: var(--backdrop);
  }
  .sheet { position: relative; width: 1200px; height: 1200px; }
  .card {
    position: absolute; left: 257px; width: 686px; height: 392px;
  }
  .card--front {
    top: 165px;
    background: radial-gradient(ellipse at 55% 20%, #3b3b3b 0%, #1c1c1c 60%, #141414 100%);
  }
  .card--back {
    top: 653px;
    background: linear-gradient(to bottom, var(--card-top) 0%, var(--card-mid) 60%, var(--card-bottom) 100%);
  }
  .card__name {
    position: absolute; top: 140px; left: 0; right: 0;
    text-align: center;
    font-family: "Playball", cursive;
    font-size: 72px; line-height: 1;
    color: var(--gold);
  }
  .card__rule {
    position: absolute; top: 292px; left: 321px; width: 44px; height: 2px;
    background: var(--rule);
  }
  .card__contact {
    position: absolute; left: 0; right: 0;
    text-align: center;
    font-family: "Quicksand", sans-serif; font-weight: 400;
    font-size: 15.5px; letter-spacing: 0.2px;
    color: var(--ink-light);
    text-transform: uppercase;
  }
  .card__contact--line1 { top: 306px; }
  .card__contact--line2 { top: 332px; }
  .card__contact .sep { margin: 0 6px; }

  .badge {
    position: absolute; top: 89px; left: 238px; width: 210px; height: 210px;
    border-radius: 50%;
    background: var(--badge-bg);
    border: 2px solid var(--gold);
    display: flex; flex-direction: column; align-items: center; justify-content: center;
    font-family: "Quicksand", sans-serif; font-weight: 400;
    color: var(--badge-ink);
    font-size: 22px; line-height: 1.15; text-align: center;
  }
  .socials {
    position: absolute; top: 340px; left: 0; right: 0;
    display: flex; justify-content: center; align-items: center; gap: 16px;
    font-family: "Quicksand", sans-serif; font-weight: 400;
    font-size: 16px; color: var(--ink-light);
  }
  .socials__item { display: flex; align-items: center; gap: 11px; }
  .socials__mark { width: 21px; height: 21px; background: var(--ink-light); border-radius: 4px; }
  .socials__mark--round { border-radius: 50%; }
</style>
</head>
<body>
<main class="sheet">
  <section class="card card--front">
    <h1 class="card__name">DJ Marlow K</h1>
    <div class="card__rule"></div>
    <p class="card__contact card__contact--line1">415.282.6047<span class="sep">|</span>bxdjmarlowk@quillmail.example</p>
    <p class="card__contact card__contact--line2">www.djmarlowk.example</p>
  </section>

  <section class="card card--back">
    <div class="badge">Nightfall<br>Sessions</div>
    <div class="socials">
      <span class="socials__item"><span class="socials__mark"></span>DJMARLOWK</span>
      <span class="socials__item"><span class="socials__mark socials__mark--round"></span>DJMARLOW.K</span>
    </div>
  </section>
</main>
</body>
</html>
```